A label for a bottle of Gin that reflect the area in which it is made - Wirral

I have attached a couple of labels that we are not very happy with. We are looking for something that portrays a premium brand. The bottle is called Verbelle 700ml. and the image should be max 9cm by 7cm. For details on webpage - see notes at quellon.co.uk/farrow and quellon.co.uk/farrowgin. The website should just be a single homepage with a link to quellon.co.uk/farrowgin

The words "Small Batch Handmade Gin" could feature

Number of Pages Required

1 page

Requirements
Nice to have
• Gold or Silver that can add to overall quality feel of the label.
Should not have
• Transparent labels look great when back lit but tend to disappear when on a dark bar with other brighter bottles. Avoid transparency

```html
<!DOCTYPE html>
<html lang="en">
<head>
<meta charset="UTF-8">
<title>Verbelle Gin Label</title>
<link rel="stylesheet" href="https://fonts.googleapis.com/css2?family=Julius+Sans+One&family=Montserrat:wght@400;700&display=swap">
<style>
  :root {
    --page-bg: #ffffff;
    --night-deep: #020408;
    --night-mid: #0b1524;
    --night-glow: #1d3558;
    --ink-white: #ffffff;
    --ink-silver: #c9ced6;
    --ink-muted: #9aa0a8;
  }
  * { box-sizing: border-box; margin: 0; padding: 0; }
  html, body {
    width: 1200px;
    height: 1123px;
    overflow: hidden;
    background: var(--page-bg);
  }
  .canvas {
    position: relative;
    width: 1200px;
    height: 1123px;
  }
  .label {
    position: absolute;
    left: 218px;
    top: 71px;
    width: 764px;
    height: 980px;
    overflow: hidden;
    background: var(--night-deep);
  }
  .night-sky {
    position: absolute;
    inset: 0;
    background:
      radial-gradient(circle at 232px 206px, var(--night-glow) 0, rgba(29,53,88,0.55) 160px, rgba(11,21,36,0) 380px),
      radial-gradient(ellipse 520px 160px at 380px 560px, rgba(42,58,82,0.75) 0, rgba(42,58,82,0) 100%),
      radial-gradient(ellipse 300px 120px at 120px 620px, rgba(42,58,82,0.55) 0, rgba(42,58,82,0) 100%),
      radial-gradient(ellipse 300px 130px at 660px 620px, rgba(42,58,82,0.5) 0, rgba(42,58,82,0) 100%),
      linear-gradient(180deg, var(--night-mid) 0%, #0a1322 45%, #050a12 75%, var(--night-deep) 100%);
  }
  .brand-name {
    position: absolute;
    left: 0;
    right: 0;
    top: 92px;
    text-align: center;
    font-family: "Julius Sans One", sans-serif;
    font-weight: 400;
    font-size: 148px;
    line-height: 1;
    letter-spacing: 4px;
    color: var(--ink-white);
  }
  .tagline {
    position: absolute;
    left: 0;
    right: 0;
    top: 398px;
    text-align: center;
    font-family: "Julius Sans One", sans-serif;
    font-size: 56px;
    line-height: 64px;
    letter-spacing: 7px;
    color: var(--ink-silver);
  }
  .descriptor {
    position: absolute;
    left: 0;
    right: 0;
    top: 752px;
    text-align: center;
    font-family: "Montserrat", sans-serif;
    font-weight: 400;
    font-size: 27px;
    line-height: 34px;
    letter-spacing: 3px;
    color: var(--ink-muted);
  }
  .specs {
    position: absolute;
    left: 57px;
    right: 30px;
    top: 906px;
    display: flex;
    justify-content: space-between;
    font-family: "Montserrat", sans-serif;
    font-size: 38px;
    letter-spacing: 4px;
    color: var(--ink-white);
  }
  .specs strong { font-weight: 700; }
</style>
</head>
<body>
  <main class="canvas">
    <section class="label">
      <div class="night-sky" role="img" aria-label="Night sky with a glowing full moon above dark drifting clouds"></div>
      <h1 class="brand-name">Verbelle</h1>
      <p class="tagline">MIDNIGHT.<br>FULLMOON.<br>GIN &amp; YOU.</p>
      <p class="descriptor">SMALL BATCH<br>HANDMADE GIN</p>
      <div class="specs">
        <span><strong>700</strong>ml</span>
        <span><strong>42</strong>%acl</span>
      </div>
    </section>
  </main>
</body>
</html>
```